Reiki business card

Please see uploaded files. There is a word document on there explaining what is required and what the other uploaded files are for. I am after a soft, relaxing, warm welcoming feel to the card. Thank you.

Business

```html
<!DOCTYPE html>
<html lang="en">
<head>
<meta charset="utf-8">
<title>Calm Paws Reiki &amp; Little Hands – Business Card</title>
<link rel="stylesheet" href="https://fonts.googleapis.com/css2?family=Satisfy&display=swap">
<style>
  :root {
    --page: #ffffff;
    --teal: #19a7bc;
    --teal-light: #62c8d8;
    --teal-deep: #12768f;
    --mist: #8fd3e0;
    --ink: #ffffff;
  }
  * { margin: 0; padding: 0; box-sizing: border-box; }
  html, body {
    width: 960px;
    height: 1200px;
    overflow: hidden;
    background: var(--page);
  }
  .sheet {
    position: relative;
    width: 960px;
    height: 1200px;
  }
  .card {
    position: absolute;
    left: 60px;
    width: 840px;
    height: 480px;
    overflow: hidden;
    color: var(--ink);
    font-family: "Satisfy", cursive;
    font-weight: 400;
    background:
      radial-gradient(circle at 18% 30%, var(--teal-deep) 0%, transparent 28%),
      radial-gradient(circle at 70% 70%, var(--teal-deep) 0%, transparent 30%),
      radial-gradient(circle at 45% 60%, var(--mist) 0%, transparent 25%),
      radial-gradient(circle at 85% 25%, var(--teal-light) 0%, transparent 30%),
      radial-gradient(circle at 10% 80%, var(--teal-light) 0%, transparent 30%),
      linear-gradient(135deg, var(--teal) 0%, var(--teal-light) 50%, var(--teal) 100%);
  }
  .card--front { top: 62px; }
  .card--back  { top: 657px; }

  .tree-art {
    position: absolute;
    left: 0;
    top: 0;
    width: 360px;
    height: 480px;
  }

  .business-name {
    position: absolute;
    left: 370px;
    top: 86px;
    width: 444px;
    text-align: center;
    font-weight: 400;
    font-size: 58px;
    line-height: 100px;
    white-space: nowrap;
  }
  .contact {
    position: absolute;
    left: 578px;
    top: 390px;
    white-space: nowrap;
  }
  .contact__name {
    font-size: 32px;
    line-height: 40px;
    letter-spacing: 0.5px;
  }
  .contact__phone {
    font-size: 25px;
    line-height: 34px;
    padding-left: 10px;
  }

  .tagline {
    position: absolute;
    left: 0;
    top: 96px;
    width: 100%;
    text-align: center;
    font-size: 54px;
    line-height: 72px;
    white-space: nowrap;
  }
  .email {
    position: absolute;
    left: 0;
    top: 360px;
    width: 100%;
    text-align: center;
    font-size: 34px;
    line-height: 40px;
    letter-spacing: 2px;
    white-space: nowrap;
  }
</style>
</head>
<body>
<main class="sheet">
  <section class="card card--front">
    <svg class="tree-art" viewBox="0 0 360 480" role="img" aria-label="White silhouette of a large tree with a dog and a child sitting beneath it">
      <defs>
        <radialGradient id="treeGlow" cx="35%" cy="38%" r="65%">
          <stop offset="0%" stop-color="#ffffff" stop-opacity="1"/>
          <stop offset="70%" stop-color="#ffffff" stop-opacity="0.95"/>
          <stop offset="100%" stop-color="#ffffff" stop-opacity="0"/>
        </radialGradient>
      </defs>
      <rect x="0" y="0" width="360" height="480" fill="url(#treeGlow)"/>
    </svg>
    <h1 class="business-name">Calm Paws Reiki<br>&amp; Little Hands</h1>
    <div class="contact">
      <p class="contact__name">Maren Holloway</p>
      <p class="contact__phone">0400 218 764</p>
    </div>
  </section>

  <section class="card card--back">
    <p class="tagline">Reiki - relaxes, restores balance<br>&amp; promotes healing</p>
    <p class="email">calmpawsandlittlehands@mailbox.com</p>
  </section>
</main>
</body>
</html>
```